Brisko Sky Park needs a new upscale business card design for our high end aircraft hangar complex

Brisko Sky Park (BSP) is a large, upscale jet hangar complex in the US housing expensive aircraft. We need a new business card design, using our current logo. We will be attending a industry convention and need a card design that will stand out and be remembered by aircraft owners and private pilots.

Target Market(s)

Aircraft pilots or owners looking for a new upscale hangar

Industry/Entity Type

Airport

Contact Information for Business Card

I like to use very heavy card stock, 400#, double sided. Square, no rounded edges please.

Colors
3276b5
0255a3
85abd2

Requirements
Must have
• An expensive, classy design, vivid colors.
Nice to have
• Needs to look very expensive and classy, and have some "pop". Designer must be able to download or copy my current typeface or fonts.
• One card side might be black with the "Logo and Brisko Sky Park Double line image in blue (or try gold, or glossy black), and perhaps have a grayed out "K480 jet silhouette". The other card side would have our contact info, and perhaps the "BSP Logo only". I'd like my contact info 'stacked', not in a paragraph format.
Should not have
• Should not look "too busy". Having a double-sided card will help.

```html
<!DOCTYPE html>
<html lang="en">
<head>
<meta charset="UTF-8">
<title>Brisko Sky Park – Business Card</title>
<link rel="stylesheet" href="https://fonts.googleapis.com/css2?family=Montserrat:wght@500;700&family=Open+Sans:wght@500&display=swap">
<style>
  :root {
    --card-black: #030607;
    --gold-light: #f3dc8a;
    --gold-mid: #e0ad55;
    --gold-deep: #a8702e;
    --name-yellow: #ffd200;
    --contact-yellow: #f6c915;
    --icon-ink: #1a1206;
    --page-white: #ffffff;
  }
  * { box-sizing: border-box; margin: 0; padding: 0; }
  html, body {
    width: 1025px; height: 1200px; overflow: hidden;
    background: var(--page-white);
  }
  .sheet { position: relative; width: 1025px; height: 1200px; }

  .card {
    position: absolute; left: 0; width: 1025px; height: 585px;
    background: var(--card-black); overflow: hidden;
  }
  .card--front { top: 0; }
  .card--back { top: 615px; }

  .front-frame {
    position: absolute; left: 16px; top: 27px; width: 989px; height: 534px;
    border: 4px solid var(--gold-mid);
    border-image: linear-gradient(90deg, var(--gold-light), var(--gold-deep) 40%, var(--gold-light) 70%, var(--gold-mid)) 1;
  }

  .brand-initials {
    position: absolute;
    font-family: "Montserrat", sans-serif; font-weight: 700;
    color: var(--gold-mid); letter-spacing: 4px; line-height: 1;
  }
  .brand-initials--front { left: 48px; top: 222px; font-size: 78px; }
  .brand-initials--back { left: 706px; top: 70px; font-size: 104px; }
  .brand-initials__dot {
    display: inline-block; width: 18px; height: 18px; border-radius: 50%;
    background: var(--gold-mid); margin-left: 10px; vertical-align: middle;
  }

  .brand-name {
    position: absolute; left: 318px; top: 176px;
    font-family: "Montserrat", sans-serif; font-weight: 700;
    color: var(--gold-mid); text-transform: uppercase; line-height: 1.05;
  }
  .brand-name__line { display: block; font-size: 80px; }
  .brand-name__line--sub { font-size: 62px; letter-spacing: 2px; }

  .jet-art {
    position: absolute;
    background: linear-gradient(160deg, rgba(190,190,190,0.35), rgba(224,173,85,0.55));
    border-radius: 6px;
  }
  .jet-art--front { left: 803px; top: 431px; width: 176px; height: 107px; }
  .jet-art--back { left: 842px; top: 486px; width: 161px; height: 74px; }

  .sweep { position: absolute; left: 0; top: 0; }

  .holder-name {
    position: absolute; left: 59px; top: 62px;
    font-family: "Montserrat", sans-serif; font-weight: 500;
    font-size: 56px; color: var(--name-yellow); letter-spacing: 1px;
  }

  .contact-list { position: absolute; left: 54px; top: 266px; list-style: none; }
  .contact-list__item {
    display: flex; align-items: center; height: 44px; margin-bottom: 36px;
    font-family: "Open Sans", sans-serif; font-weight: 500;
    font-size: 27px; color: var(--contact-yellow);
  }
  .contact-list__item:nth-child(3) { margin-bottom: 38px; }
  .contact-list__icon {
    width: 43px; height: 43px; border-radius: 50%; margin-right: 24px; flex: none;
    background: radial-gradient(circle at 35% 30%, var(--gold-light), var(--gold-mid) 55%, var(--gold-deep));
    display: flex; align-items: center; justify-content: center;
  }
  .contact-list__icon svg { width: 24px; height: 24px; fill: var(--icon-ink); }
</style>
</head>
<body>
<div class="sheet">

  <section class="card card--front" aria-label="Card front">
    <div class="front-frame"></div>
    <div class="brand-initials brand-initials--front">BSP<span class="brand-initials__dot"></span></div>
    <h1 class="brand-name">
      <span class="brand-name__line">Brisko</span>
      <span class="brand-name__line brand-name__line--sub">Sky Park</span>
    </h1>
    <div class="jet-art jet-art--front" role="img" aria-label="Business jet in flight with gold speed streaks"></div>
  </section>

  <section class="card card--back" aria-label="Card back">
    <svg class="sweep" width="1025" height="585" viewBox="0 0 1025 585" aria-hidden="true">
      <defs>
        <linearGradient id="sweepGold" x1="0" y1="0" x2="0" y2="1">
          <stop offset="0" stop-color="#f3dc8a"/>
          <stop offset="0.45" stop-color="#a8702e"/>
          <stop offset="1" stop-color="#e0ad55"/>
        </linearGradient>
      </defs>
      <path d="M465 0 Q770 190 812 585 L772 585 Q725 210 465 0 Z" fill="url(#sweepGold)"/>
    </svg>

    <h2 class="holder-name">Your Name</h2>

    <ul class="contact-list">
      <li class="contact-list__item">
        <span class="contact-list__icon"><svg viewBox="0 0 24 24"><path d="M6.6 10.8a15.1 15.1 0 0 0 6.6 6.6l2.2-2.2a1 1 0 0 1 1-.25 11.4 11.4 0 0 0 3.6.57 1 1 0 0 1 1 1V20a1 1 0 0 1-1 1A17 17 0 0 1 3 4a1 1 0 0 1 1-1h3.5a1 1 0 0 1 1 1c0 1.25.2 2.45.57 3.57a1 1 0 0 1-.25 1z"/></svg></span>
        +1 123-456-7890
      </li>
      <li class="contact-list__item">
        <span class="contact-list__icon"><svg viewBox="0 0 24 24"><path d="M12 2a10 10 0 1 0 0 20 10 10 0 0 0 0-20zm6.9 6h-2.9a15.6 15.6 0 0 0-1.4-3.6A8 8 0 0 1 18.9 8zM12 4c.8 1.2 1.5 2.5 1.9 4h-3.8c.4-1.5 1.1-2.8 1.9-4zM4.3 14a8 8 0 0 1 0-4h3.4a16 16 0 0 0 0 4zm.8 2h2.9c.3 1.3.8 2.5 1.4 3.6A8 8 0 0 1 5.1 16zM8 8H5.1a8 8 0 0 1 4.3-3.6C8.8 5.5 8.3 6.7 8 8zm4 12c-.8-1.2-1.5-2.5-1.9-4h3.8c-.4 1.5-1.1 2.8-1.9 4zm2.3-6H9.7a14 14 0 0 1 0-4h4.6a14 14 0 0 1 0 4zm.3 5.6c.6-1.1 1.1-2.3 1.4-3.6h2.9a8 8 0 0 1-4.3 3.6zm1.7-5.6a16 16 0 0 0 0-4h3.4a8 8 0 0 1 0 4z"/></svg></span>
        www.yoursite.com
      </li>
      <li class="contact-list__item">
        <span class="contact-list__icon"><svg viewBox="0 0 24 24"><path d="M3 5h18v14H3zm2 2v.4l7 4.6 7-4.6V7zm0 2.8V17h14V9.8l-7 4.6z"/></svg></span>
        contact@yoursite.com
      </li>
      <li class="contact-list__item">
        <span class="contact-list__icon"><svg viewBox="0 0 24 24"><path d="M12 2a7 7 0 0 0-7 7c0 5.2 7 13 7 13s7-7.8 7-13a7 7 0 0 0-7-7zm0 9.5A2.5 2.5 0 1 1 12 6.5a2.5 2.5 0 0 1 0 5z"/></svg></span>
        Street Address, city, USA
      </li>
    </ul>

    <div class="brand-initials brand-initials--back">BSP</div>
    <div class="jet-art jet-art--back" role="img" aria-label="Small business jet with gold speed streaks"></div>
  </section>

</div>
</body>
</html>
```